Stationery Design Project

We need a stationery design for a consultancy called 'Marlow Ridge'. The design should communicate innovation and professionalism. The colors used should complement our logo. Please include source files for winning design.

Requirements
Must have
• Logo with company name should be included. Font of the text in logo should not be altered. Paper should be A4 sized and not Letter sized.

```html
<!DOCTYPE html>
<html lang="en">
<head>
<meta charset="utf-8">
<title>Marlow Ridge — Stationery</title>
<link rel="stylesheet" href="https://fonts.googleapis.com/css2?family=Cinzel:wght@600&family=Arimo:wght@400&family=Questrial&display=swap">
<style>
  :root {
    --backdrop: #e7e7e7;
    --paper: #ffffff;
    --ink: #1a1a1a;
    --brand-black: #050505;
    --brand-orange: #f08a1c;
    --name-light: #ffffff;
    --rule: #222222;
    --sketch-tone: #efefef;
  }
  * { margin: 0; padding: 0; box-sizing: border-box; }
  html, body { width: 1200px; height: 923px; overflow: hidden; }
  body { background: var(--backdrop); position: relative; font-family: "Arimo", Arial, sans-serif; color: var(--ink); }

  .letterhead { position: absolute; left: 171px; top: 68px; width: 520px; height: 770px; background: var(--paper); }
  .name-block { position: absolute; background: var(--brand-black); display: flex; align-items: center; justify-content: center; }
  .name-block .square { background: var(--brand-orange); flex: none; }
  .name-block .company { font-family: "Questrial", sans-serif; font-weight: 400; color: var(--name-light); white-space: nowrap; }
  .letterhead .name-block { left: 0; top: 31px; width: 128px; height: 81px; gap: 7px; }
  .letterhead .name-block .square { width: 10px; height: 10px; }
  .letterhead .name-block .company { font-size: 12px; }

  .letter-body { position: absolute; left: 148px; top: 181px; width: 344px; font-size: 7.9px; line-height: 12.1px; text-align: justify; }
  .letter-body p + p { margin-top: 12.1px; }
  .signature { position: absolute; left: 151px; top: 514px; width: 110px; height: 40px; background: linear-gradient(90deg, #f3f3f3, #e9e9e9); }

  .contact { font-family: "Questrial", sans-serif; font-size: 7.6px; line-height: 11px; }
  .contact .web { color: var(--brand-orange); }
  .letterhead .contact { position: absolute; left: 44px; top: 680px; }
  .letterhead .contact .web { margin-top: 8px; }
  .sketch { position: absolute; background: linear-gradient(180deg, var(--paper), var(--sketch-tone)); }
  .letterhead .sketch { left: 394px; top: 680px; width: 100px; height: 74px; }
  .base-rule { position: absolute; height: 1px; background: var(--rule); }
  .letterhead .base-rule { left: 19px; top: 754px; width: 480px; }

  .card-front { left: 855px; top: 69px; width: 222px; height: 141px; gap: 12px; }
  .card-front .square { width: 16px; height: 16px; }
  .card-front .company { font-size: 20px; }

  .card-back { position: absolute; left: 853px; top: 254px; width: 220px; height: 139px; background: var(--paper); }
  .card-back .name { position: absolute; left: 31px; top: 13px; font-family: "Cinzel", serif; font-weight: 600; font-size: 10px; color: var(--brand-orange); }
  .card-back .role { position: absolute; left: 31px; top: 30px; font-family: "Questrial", sans-serif; font-size: 7.6px; font-style: italic; }
  .card-back .contact { position: absolute; right: 24px; top: 56px; text-align: right; }
  .card-back .contact .web { margin-top: 9px; }
  .card-back .sketch { left: 5px; top: 55px; width: 84px; height: 70px; }
  .card-back .base-rule { left: 5px; top: 125px; width: 195px; }
</style>
</head>
<body>
  <section class="letterhead">
    <div class="name-block">
      <div class="square"></div>
      <div class="company">Marlow Ridge</div>
    </div>
    <div class="letter-body">
      <p>Lorem ipsum dolor sit amet, consectetur adipiscing elit. Suspendisse blandit, nulla ut porta scelerisque, urna massa ultrices ligula, at rutrum nunc ipsum ac risus. Sed consectetur nulla non velit sollicitudin a eleifend tortor pellentesque. Cras laoreet iaculis pretium. Vestibulum vitae sapien at metus fermentum tempus quis sed mauris. Donec blandit metus in nibh laoreet ultrices. Nullam molestie, turpis ac adipiscing tincidunt, urna justo eleifend ligula, et consectetur massa lorem ac risus. Aenean quis justo vitae massa accumsan ultricies posuere eget diam. Aenean ipsum sapien, pellentesque id semper vitae, mattis eget enim. Vestibulum congue tincidunt enim ut tristique. Praesent interdum malesuada adipiscing. Donec quis felis massa.</p>
      <p>Praesent nisi libero, pretium eu interdum eu, rhoncus ut lorem. Praesent faucibus lorem sit amet ligula consequat adipiscing. Morbi adipiscing dapibus erat, eu condimentum nibh vestibulum vel. In elementum nulla id arcu bibendum malesuada. Donec non nulla sit amet tortor volutpat placerat id vel felis. Maecenas accumsan, augue ac molestie iaculis, justo risus vestibulum dolor, eu ullamcorper nulla orci ac est. Donec tristique sem a nisl euismod convallis id ac lacus. Sed pretium bibendum velit eget mollis. Praesent porta suscipit lacus, ac porta odio faucibus eu. Donec accumsan laoreet nisi et hendrerit. In fringilla enim ac urna sagittis convallis.</p>
      <p>Nullam est mi, euismod ac pretium ac, consequat eu urna. Aliquam egestas, elit non gravida pellentesque, purus orci facilisis est, vitae ultricies turpis nisl non justo. Fusce varius libero nec nibh elementum consequat ut sed elit. Integer lorem erat, varius ac malesuada vitae, convallis sit amet libero. Cras sagittis, urna eu scelerisque auctor, elit tellus vestibulum mi, non elementum metus eros ut dolor. Etiam porta est dolor. Vivamus suscipit lobortis commodo. Integer convallis, nunc tincidunt rhoncus lobortis, sapien purus ultrices orci, quis dignissim urna felis dictum elit.</p>
    </div>
    <div class="signature" role="img" aria-label="Handwritten signature"></div>
    <div class="contact">
      <div>Firm Address</div>
      <div>(+00) 123&nbsp; 456 7890</div>
      <div>(+00) 123&nbsp; 456 7890</div>
      <div>info@marlowridge.com</div>
      <div class="web">www.marlowridge.com</div>
    </div>
    <div class="sketch" role="img" aria-label="Line drawing of a lighthouse on rocks"></div>
    <div class="base-rule"></div>
  </section>

  <section class="card-front name-block">
    <div class="square"></div>
    <div class="company">Marlow Ridge</div>
  </section>

  <section class="card-back">
    <div class="name">Name Surname</div>
    <div class="role">Administrator</div>
    <div class="sketch" role="img" aria-label="Line drawing of a lighthouse on rocks"></div>
    <div class="contact">
      <div>Firm Address</div>
      <div>(+00) 123&nbsp; 456 7890</div>
      <div>(+00) 123&nbsp; 456 7890</div>
      <div>info@marlowridge.com</div>
      <div class="web">www.marlowridge.com</div>
    </div>
    <div class="base-rule"></div>
  </section>
</body>
</html>
```